Marketplace Web Re-design overhaul @quarrynest

Hi,
We are currently in production with a website that is getting some mixed feedback about visual appeal and usability. We are using a responsive design and need to stay true to the logo colours and other marketing collateral we have in place. I will provide a brochure with the colour palate we use for some guidance. If you can please help us design something fresh and modern to communicate the essence of our company. The brochure will be a good summary of what we do and who we are targeting as customers. Our current website can be found at www.quarrynest.com. If there is any questions, please let me know.

Target Market(s)

Contractors and Corporate Companies

Industry/Entity Type

Information Technology

Number of Pages Required

4 page

Requirements
Must have
• Must have a complete new visual look, including
• 1. Images
• 2. Background colour scheme overhaul (not black)
• 3. re-design of the layout but keep to similar page breakdowns
Nice to have
• Some of the pages are a bit wordy, happy to have suggestions on how to reduce.
• Would be great if we can integrate the Plumb.ON! blog page to the Quarrynest page?
• This is some feedback a fellow UX designer provided to improve our CRO
• First off when you land on the home page, who is your audience? Are you everything to everyone? Even after watching the video (https://www.vidmarrow.net/watch?v=q7RtPe3LwZ0), I do not know what markets you service or who this app will be for.
• Your main headline and paragraph above the fold I find unnecessarily wordy and an overuse of 'buzzwords' . Perhaps you could look at appealing to the lowest common denominator and make it very simple and put it all into a simple sentence.
• The main hero image to the right of the headline offers no emotional pull at all. I'm assuming it's just a screenshot of your dashboard? Personally, I would be looking at using a person's image in that space.
• Also in this space, increase the size of your 'register' button. On the topic of your register button, you have it in different colours. Green in header, and red in content. Make it the same colour, and don't use that colour again on the site. That colour is to become your call to action (CTA) colour. Understandably you'll have three different colours for the account type, and again, don't use these colours anywhere else on the site.
• The registration area where the three account types are where you choose which one suits you, it's extremely busy with background images and heavy use of text. If you were my client, I would be advising you to ditch the bg image (including the Zelo shot), keeping the text, making the register icons much bigger. Perhaps instead of bg images, use a solid colour for each (green, orange, red). I'm highly confident this change will make a massive difference in your sign up rate.
Should not have
• Please keep to the fonts used on the original website
• Keep to the colour provided on the company brochure for guidance.

```html
<!DOCTYPE html>
<html lang="en">
<head>
<meta charset="utf-8">
<title>Quarrynest – Home</title>
<link href="https://fonts.googleapis.com/css2?family=Raleway:wght@400;500;600&family=Lato:wght@400;700&display=swap" rel="stylesheet">
<style>
:root{
  --green:#2e9a4a;
  --green-dark:#1f7a36;
  --green-text:#39a935;
  --orange:#f58220;
  --red:#d83a32;
  --ink:#333;
  --muted:#555;
  --paper:#ececec;
  --paper-light:#f3f3f3;
  --dark:#1c1c1c;
  --darker:#111;
  --white:#fff;
}
*{box-sizing:border-box;margin:0;padding:0}
html,body{width:1200px;height:2951px;overflow:hidden}
body{font-family:"Lato",Arial,sans-serif;color:var(--ink);background:var(--white);position:relative}
.abs{position:absolute}
.heading{font-family:"Raleway",Arial,sans-serif;font-weight:500;color:#333;text-align:center;font-size:31px}
.rule{width:56px;height:3px;margin:12px auto 0;background:linear-gradient(90deg,var(--green) 50%,var(--red) 50%)}
.btn{display:inline-block;color:#fff;font-family:"Raleway",sans-serif;font-size:17px;padding:6px 0;text-align:center;border-radius:2px}
.btn-green{background:var(--green);border:1px solid #1a6d2e}
.btn-orange{background:var(--orange)}

/* header */
.site-header{top:0;left:0;width:1200px;height:110px;background:#fff}
.logo{left:165px;top:40px;display:flex;align-items:center;gap:10px}
.logo .dot{width:30px;height:30px;border-radius:50%;background:var(--green)}
.logo span{font-family:"Raleway",sans-serif;font-size:28px;color:#666;font-weight:500}
.social{display:flex;gap:7px}
.social i{width:19px;height:19px;border-radius:50%;background:var(--green);display:block}
.top-social{left:548px;top:8px}
.phone-tab{left:676px;top:0;width:176px;height:36px;background:var(--orange);color:#fff;font-size:18px;font-weight:700;display:flex;align-items:center;justify-content:center;gap:8px;border-radius:0 0 0 16px}
.login-tab{left:852px;top:0;width:178px;height:36px;background:#f1f1f1;font-size:18px;color:var(--green);display:flex;align-items:center;justify-content:center}
.login-tab b{font-weight:400;color:#999;margin:0 5px}
.login-tab em{font-style:normal;color:var(--red)}
.main-nav{left:450px;top:60px;display:flex;gap:0;font-family:"Raleway",sans-serif;font-size:14px;color:#555}
.main-nav a{padding:0 11px;border-right:1px solid #ddd;line-height:16px;color:#555;text-decoration:none}
.main-nav a:last-child{border:0}
.main-nav a.active{color:var(--red);border-bottom:2px solid var(--red);padding-bottom:10px}

/* hero */
.hero{top:110px;left:0;width:1200px;height:390px;background:radial-gradient(circle at 80% 55%,#dff6f4 0,#6fb0ab 12%,#2a5a5d 35%,#1f3c44 70%,#1a2e35 100%)}
.slider-arrow{width:40px;height:40px;border-radius:50%;border:2px solid rgba(255,255,255,.7);background:rgba(0,0,0,.35)}
.hero-band{top:500px;left:0;width:1200px;height:60px;background:linear-gradient(#36a55a,#1f7d3c);display:flex;align-items:center;justify-content:center;gap:40px}
.hero-band h1{font-family:"Raleway",sans-serif;font-weight:500;font-size:30px;color:#fff}
.hero-band .btn{width:110px;font-size:17px;font-weight:600}

/* welcome */
.welcome{top:560px;left:0;width:1200px;height:270px;background:var(--paper);padding-top:30px}
.welcome p{width:750px;margin:30px auto 0;text-align:center;font-size:13.5px;line-height:24px;color:#444}
.welcome .btn{width:126px;position:absolute;left:537px;top:208px}

/* video */
.video{top:830px;left:0;width:1200px;height:425px;background:var(--paper-light);padding-top:35px}
.video-media{left:365px;top:110px;width:470px;height:315px;background:linear-gradient(#e9e9e9,#cfcfcf);border-radius:6px}
.play{left:577px;top:241px;width:54px;height:36px;background:var(--red);border-radius:8px}

/* audience split */
.audience{top:1255px;width:600px;height:410px;color:#fff;padding:60px 0 0}
.audience.contractors{left:0;background:linear-gradient(135deg,#c94538,#b83a2e)}
.audience.employers{left:600px;background:linear-gradient(135deg,#3d3f42,#2a2b2d)}
.audience h2{font-family:"Raleway",sans-serif;font-weight:500;font-size:29px}
.audience p{font-size:13px;line-height:24px;margin-top:18px}
.audience ul{list-style:none;margin-top:12px;font-size:13px;line-height:28px}
.audience li{display:flex;align-items:center;gap:10px}
.contractors .inner{margin-left:160px;width:380px}
.employers .inner{margin-left:65px;width:380px;text-align:right}
.employers li{justify-content:flex-end}
.employers li svg{order:2}
.audience .btn{width:126px;margin-top:28px}
.under-red{width:56px;height:2px;background:#fff;margin-top:8px}
.under-mix{width:56px;height:2px;margin:8px 0 0 auto;background:linear-gradient(90deg,var(--green) 50%,var(--red) 50%)}

/* blog */
.blog{top:1665px;left:0;width:1200px;height:410px;background:var(--paper-light);padding-top:40px}
.post{display:flex;gap:12px;width:380px}
.thumb{width:113px;height:80px;background:linear-gradient(#e5e7ea,#9aa3ad)}
.post h3{font-size:14px;color:var(--green-text);font-weight:700}
.post .date{font-size:13px;margin:5px 0 4px}
.post p{font-size:13px;line-height:19px;color:#333}
.blog-divider{left:590px;top:110px;width:1px;height:160px;background:#d5d5d5}
.round-arrow{width:32px;height:32px;border-radius:50%;background:#3a3a3a}

/* team */
.team{top:2075px;left:0;width:1200px;height:500px;background:var(--paper);padding-top:18px}
.member{top:98px;width:248px;height:333px;background:linear-gradient(#2c9a47,#1c7a35);color:#fff;text-align:center;padding:14px 15px 0}
.member .photo{width:218px;height:145px;background:linear-gradient(#d9d1c7,#7a6a60)}
.member h3{font-size:14px;font-weight:700;margin-top:10px;color:#e8f5ea}
.member h4{font-size:13px;font-weight:700;margin-top:10px}
.member p{font-size:12px;line-height:18px;color:#d8efdc;margin-top:10px}
.member .mail{font-size:12px;font-weight:700;margin-top:18px}

/* footer */
.swoosh{top:2500px;left:0}
.site-footer{top:2620px;left:0;width:1200px;height:290px;background:var(--dark);color:#ccc}
.site-footer h4{font-family:"Raleway",sans-serif;font-weight:500;font-size:15px;color:#ddd}
.site-footer .line{height:1px;background:#3a3a3a;margin-top:10px;width:220px}
.links{display:grid;grid-template-columns:100px 100px;font-size:11px;line-height:24px;margin-top:8px}
.links a{color:#ccc;text-decoration:none}
.links a.active{color:var(--orange)}
.contact div{display:flex;gap:10px;font-size:11px;line-height:15px;margin-top:12px}
.contact .big{font-size:14px}
.news p{font-size:11px;line-height:15px;margin-top:12px;width:170px}
.news .field{width:170px;height:24px;background:#fff;margin-top:14px;font-size:9px;color:#888;padding:6px}
.news .btn{width:80px;font-size:12px;margin-top:14px;padding:3px 0}
.foot-logo{left:900px;top:110px;text-align:center;width:130px}
.foot-logo .dot{width:34px;height:34px;border-radius:50%;background:var(--green);margin:0 auto}
.foot-logo span{display:block;font-family:"Raleway",sans-serif;font-size:24px;color:#bbb;margin-top:6px}
.foot-logo .social{justify-content:center;margin-top:12px}
.foot-logo .social i{background:#555}
.copyright{top:2910px;left:0;width:1200px;height:41px;background:var(--darker);color:#bbb;font-size:11px;text-align:center;line-height:41px}
</style>
</head>
<body>

<header class="site-header abs">
  <div class="logo abs"><i class="dot"></i><span>Quarrynest</span></div>
  <div class="social top-social abs"><i></i><i></i><i></i><i></i></div>
  <div class="phone-tab abs">
    <svg width="18" height="18" viewBox="0 0 24 24"><circle cx="12" cy="12" r="10" fill="none" stroke="#fff" stroke-width="2"/><path d="M8 7l2 0 1 3-1.5 1a6 6 0 003 3l1-1.5 3 1v2a1 1 0 01-1 1A9 9 0 017 8a1 1 0 011-1z" fill="#fff"/></svg>
    555-014-2287
  </div>
  <div class="login-tab abs">Login<b>/</b><em>Register</em></div>
  <nav class="main-nav abs">
    <a class="active" href="#">Home</a><a href="#">How It Works</a><a href="#">About Us</a><a href="#">Our Partners</a><a href="#">FAQ's</a><a href="#">Blog</a><a href="#">Contact Us</a>
  </nav>
</header>

<section class="hero abs" role="img" aria-label="Row of hanging light bulbs with one glowing bulb on a dark teal background"></section>
<span class="slider-arrow abs" style="left:78px;top:314px"></span>
<span class="slider-arrow abs" style="left:1082px;top:314px"></span>
<div class="hero-band abs"><h1>The Future of Work is Here!</h1><span class="btn btn-orange">Get Started</span></div>

<section class="welcome abs">
  <h2 class="heading">Welcome to Quarrynest</h2><div class="rule"></div>
  <p>Lorem ipsum dolor sit amet, consectetuer adipiscing elit, sed diam nonummy nibh euismod tincidunt ut laoreet dolore magna aliquam erat volutpat. Ut wisi enim ad minim veniam, quis nostrud exerci tation ullamcorper suscipit lobortis nisl ut aliquip ex ea commodo consequat. Duis autem vel eum iriure dolor in hendrerit in vulputate velit esse molestie consequat, vel illum dolore feugiat nulla facilisis at vero eros et accumsan et iusto</p>
  <span class="btn btn-green">Read More</span>
</section>

<section class="video abs">
  <h2 class="heading">View Video</h2><div class="rule" style="background:transparent"></div>
  <div class="video-media abs" role="img" aria-label="Hands holding a Zelo tablet playing a video of two colleagues at a desk"></div>
  <span class="play abs"></span>
  <svg class="abs" style="left:596px;top:250px" width="18" height="18" viewBox="0 0 18 18"><path d="M2 1l14 8-14 8z" fill="#fff"/></svg>
</section>

<section class="audience contractors abs" role="img" aria-label="Contractor at work, tinted red">
  <div class="inner">
    <h2>For Contractors</h2><div class="under-red"></div>
    <p>Lorem ipsum dolor sit amet, consectetuer adipiscing elit, sed diam nonummy nibh euismod tincidunt ut laoreet dolore magna aliquam erat volutpat. Ut wisi enim ad minim veniam, quis nostrud exerci tation ullamcorper.</p>
    <ul>
      <li><svg width="13" height="13" viewBox="0 0 14 14"><circle cx="7" cy="7" r="6" fill="none" stroke="#fff" stroke-width="1.5"/><path d="M4 7l2 2 4-4" fill="none" stroke="#fff" stroke-width="1.5"/></svg>Lorem ipsum dolor sit amet lorem ipsum the</li>
      <li><svg width="13" height="13" viewBox="0 0 14 14"><circle cx="7" cy="7" r="6" fill="none" stroke="#fff" stroke-width="1.5"/><path d="M4 7l2 2 4-4" fill="none" stroke="#fff" stroke-width="1.5"/></svg>Lorem ipsum dolor sit amet lorem ipsum the this is ipsum</li>
      <li><svg width="13" height="13" viewBox="0 0 14 14"><circle cx="7" cy="7" r="6" fill="none" stroke="#fff" stroke-width="1.5"/><path d="M4 7l2 2 4-4" fill="none" stroke="#fff" stroke-width="1.5"/></svg>Lorem ipsum dolor sit amet lorem ipsum the</li>
    </ul>
    <span class="btn btn-green">Read More</span>
  </div>
  <svg class="abs" style="left:490px;top:58px" width="36" height="40" viewBox="0 0 36 40"><circle cx="18" cy="14" r="10" fill="#fff"/><path d="M4 40a14 14 0 0128 0z" fill="#fff"/></svg>
</section>

<section class="audience employers abs" role="img" aria-label="Business meeting, tinted dark grey">
  <svg class="abs" style="left:60px;top:58px" width="44" height="40" viewBox="0 0 44 40"><circle cx="10" cy="10" r="6" fill="#fff"/><circle cx="22" cy="8" r="7" fill="#fff"/><circle cx="34" cy="10" r="6" fill="#fff"/><rect x="4" y="18" width="12" height="20" rx="4" fill="#fff"/><rect x="15" y="17" width="14" height="23" rx="4" fill="#fff"/><rect x="28" y="18" width="12" height="20" rx="4" fill="#fff"/></svg>
  <div class="inner">
    <h2>For Employers</h2><div class="under-mix"></div>
    <p>Lorem ipsum dolor sit amet, consectetuer adipiscing elit, sed diam nonummy nibh euismod tincidunt ut laoreet dolore magna aliquam erat volutpat. Ut wisi enim ad minim veniam, quis nostrud exerci tation ullamcorper.</p>
    <ul>
      <li><svg width="13" height="13" viewBox="0 0 14 14"><circle cx="7" cy="7" r="6" fill="none" stroke="#fff" stroke-width="1.5"/><path d="M4 7l2 2 4-4" fill="none" stroke="#fff" stroke-width="1.5"/></svg>Lorem ipsum dolor sit amet lorem ipsum the</li>
      <li><svg width="13" height="13" viewBox="0 0 14 14"><circle cx="7" cy="7" r="6" fill="none" stroke="#fff" stroke-width="1.5"/><path d="M4 7l2 2 4-4" fill="none" stroke="#fff" stroke-width="1.5"/></svg>Lorem ipsum dolor sit amet lorem ipsum the this is ipsum</li>
      <li><svg width="13" height="13" viewBox="0 0 14 14"><circle cx="7" cy="7" r="6" fill="none" stroke="#fff" stroke-width="1.5"/><path d="M4 7l2 2 4-4" fill="none" stroke="#fff" stroke-width="1.5"/></svg>Lorem ipsum dolor sit amet lorem ipsum the</li>
    </ul>
    <span class="btn btn-green">Read More</span>
  </div>
</section>

<section class="blog abs">
  <h2 class="heading">Recent Blog Posts</h2><div class="rule"></div>
  <span class="blog-divider abs"></span>
  <span class="round-arrow abs" style="left:128px;top:232px"></span>
  <span class="round-arrow abs" style="left:1040px;top:232px"></span>
  <article class="post abs" style="left:195px;top:140px"><div class="thumb" role="img" aria-label="Colleagues reviewing documents"></div><div><h3>Lorem ipsum dolor sit</h3><div class="date">25th March, 2016</div><p>Lorem ipsum dolor sit amet consect, consectetur adipiscing elit integer</p></div></article>
  <article class="post abs" style="left:645px;top:140px"><div class="thumb" role="img" aria-label="Colleagues reviewing documents"></div><div><h3>Lorem ipsum dolor sit</h3><div class="date">25th March, 2016</div><p>Lorem ipsum dolor sit amet consect, consectetur adipiscing elit integer</p></div></article>
  <article class="post abs" style="left:195px;top:260px"><div class="thumb" role="img" aria-label="Colleagues reviewing documents"></div><div><h3>Lorem ipsum dolor sit</h3><div class="date">25th March, 2016</div><p>Lorem ipsum dolor sit amet consect, consectetur adipiscing elit integer</p></div></article>
  <article class="post abs" style="left:645px;top:260px"><div class="thumb" role="img" aria-label="Colleagues reviewing documents"></div><div><h3>Lorem ipsum dolor sit</h3><div class="date">25th March, 2016</div><p>Lorem ipsum dolor sit amet consect, consectetur adipiscing elit integer</p></div></article>
</section>

<section class="team abs">
  <h2 class="heading">Our Team</h2><div class="rule"></div>
  <span class="round-arrow abs" style="left:128px;top:252px"></span>
  <span class="round-arrow abs" style="left:1040px;top:252px"></span>
  <div class="member abs" style="left:183px"><div class="photo" role="img" aria-label="Portrait of team member"></div><h3>Person Name</h3><h4>Account Manager</h4><p>Sed ut perspiciatis unde omnis iste natus error sit voluptatem accusantium</p><div class="mail">owen@quarrynest.com</div></div>
  <div class="member abs" style="left:475px"><div class="photo" role="img" aria-label="Portrait of team member"></div><h3>Person Name</h3><h4>Account Manager</h4><p>Sed ut perspiciatis unde omnis iste natus error sit voluptatem accusantium</p><div class="mail">mara@quarrynest.com</div></div>
  <div class="member abs" style="left:767px"><div class="photo" role="img" aria-label="Portrait of team member"></div><h3>Person Name</h3><h4>Account Manager</h4><p>Sed ut perspiciatis unde omnis iste natus error sit voluptatem accusantium</p><div class="mail">tessa@quarrynest.com</div></div>
</section>

<svg class="swoosh abs" width="1200" height="125" viewBox="0 0 1200 125">
  <path d="M0 20 C300 150 800 110 1200 20 L1200 125 L0 125 Z" fill="#1c1c1c"/>
  <path d="M0 20 C300 130 800 100 1200 10 L1200 20 C800 112 300 150 0 40 Z" fill="#f58220"/>
</svg>

<footer class="site-footer abs">
  <div class="abs" style="left:163px;top:70px">
    <h4>Quick Links</h4><div class="line"></div>
    <div class="links"><a class="active" href="#">› Home</a><a href="#">› Blog</a><a href="#">› How It Works</a><a href="#">› Contact Us</a><a href="#">› About Us</a><span></span><a href="#">› Our Partners</a><span></span><a href="#">› FAQ's</a></div>
  </div>
  <div class="contact abs" style="left:387px;top:70px">
    <h4>Contact Information</h4><div class="line"></div>
    <div><svg width="10" height="13" viewBox="0 0 10 13"><path d="M5 0a5 5 0 00-5 5c0 4 5 8 5 8s5-4 5-8a5 5 0 00-5-5z" fill="#ccc"/></svg><span>123 euismod cidun ut laok re etmok<br>laoreet dolmopl, magnak aliquam<br>PGMCGI</span></div>
    <div class="big"><span style="margin-left:20px">555-014-2287</span></div>
    <div class="big" style="font-size:12px"><svg width="12" height="10" viewBox="0 0 12 10"><rect width="12" height="10" fill="#ccc"/><path d="M0 0l6 5 6-5" stroke="#1c1c1c" fill="none"/></svg><span>info@quarrynest.com</span></div>
  </div>
  <div class="news abs" style="left:670px;top:70px">
    <h4>Newsletter Sign Up</h4><div class="line" style="width:170px"></div>
    <p>Ut wisi enim ad minim veniam nk quis nostrud exerci tationmo.</p>
    <div class="field">Email Address</div>
    <span class="btn btn-green">Subscribe</span>
  </div>
  <div class="foot-logo abs"><div class="dot"></div><span>Quarrynest</span><div class="social"><i></i><i></i><i></i><i></i></div></div>
</footer>
<div class="copyright abs">Copyright 2016 Quarrynest. All Rights Reserved.</div>

</body>
</html>
```